Real Estate Sales and Marketing brochures

I have a few templates I uploaded of my old presentations and what I would like to see as a new presentation. I need 1 buyer (7-10 slides), 1 seller (8-12 slides), and 1 about me|us (4-5 slides) presentation. Those 3 would most likely contain 1-2 of the same slides and be 7-10 slides away. I would like it in power point presentation as well as pdf.

I am looking for something very clean, consistent, crisp, bright pictures (of the North Ga area.. Lake Morrow, North Ga Mtns, and the town of Forsyth County along with some really nice homes as the background). I have permission to use this photographers photos (he is my photographer). http://www.corvinstudio.net (go to interiors and exteriors) and http://blog.corvinstudio.net

The goal is to WoW people like my friends presentation labeled RMT does and 1: tell them what they will get with the list their home with us 2: when the buy with us and 3: who we are and what we have accomplished.

If I can get going in the right direction I would like to add stationary, letterhead, etc. to the order. My goal is to have great presentations and then have my flyers and all other printed materials match.

Target Market(s)

Buyers, sellers, and investors in the Real Estate Industry.

Industry/Entity Type

Real Estate Agent

Font styles to use
Serif

Colors
f04a50
85acd3

Requirements
Must have
• 1. about us 2. our services 3. our achievements 4. the process 5. about HB.
• Over 100m in sales (numbers and other awards can be seen at harborwithhale.net). Voted Best of Forsyth County by our Clients, 141,000 total votes, in the Ridgefield Ledger. North Ga's sole Realtor for Home Advisors We Rely On program.
Nice to have
• NICE clean pictures as the background
Should not have
• Dates on any logos or information other than achievements

```html
<!DOCTYPE html>
<html lang="en">
<head>
<meta charset="utf-8">
<title>Thank You – Jonah Hale, Harbor Bay Partners</title>
<link rel="stylesheet" href="https://fonts.googleapis.com/css2?family=Montserrat:wght@400;500;600;700&display=swap">
<style>
  :root {
    --red: #f02a2e;
    --red-deep: #e3191d;
    --red-shade: #d41d22;
    --frame-pink: #f6a4a6;
    --white: #ffffff;
    --footer: #2c2f39;
    --photo-a: #c9ccd3;
    --photo-b: #8d939e;
  }
  * { margin: 0; padding: 0; box-sizing: border-box; }
  html, body { width: 1200px; height: 900px; overflow: hidden; background: var(--red); }
  body { font-family: "Montserrat", Arial, sans-serif; color: var(--white); }

  .slide { position: relative; width: 1200px; height: 900px; overflow: hidden; }

  .backdrop {
    position: absolute; inset: 0 0 88px 0;
    background:
      radial-gradient(ellipse at 25% 55%, rgba(255,80,80,.35), transparent 60%),
      radial-gradient(ellipse at 85% 40%, rgba(180,10,15,.25), transparent 55%),
      linear-gradient(180deg, var(--red) 0%, var(--red-deep) 100%);
  }

  .project-title {
    position: absolute; left: 45px; top: 44px;
    font-size: 30px; font-weight: 700; letter-spacing: .5px;
    color: var(--red-shade); text-transform: uppercase;
  }
  .project-rule {
    position: absolute; left: 42px; top: 102px; width: 420px; height: 2px;
    background: var(--red-shade);
  }

  .thanks-heading {
    position: absolute; left: 0; right: 0; top: 154px;
    text-align: center; font-size: 42px; font-weight: 700;
    letter-spacing: .3px; text-transform: uppercase;
  }

  .agent-portrait-frame {
    position: absolute; left: 138px; top: 265px; width: 285px; height: 383px;
    background: var(--frame-pink); padding: 11px 12px;
  }
  .agent-portrait {
    width: 100%; height: 100%;
    background: linear-gradient(160deg, var(--photo-a) 0%, #e4e5e8 40%, var(--photo-b) 100%);
  }

  .agent-details { position: absolute; left: 512px; top: 272px; }
  .agent-name { font-size: 36px; font-weight: 700; line-height: 1; }
  .agent-office {
    margin-top: 24px; font-size: 15px; font-weight: 600;
    line-height: 27px; text-transform: uppercase;
  }
  .agent-contact { margin-top: 46px; font-size: 32px; font-weight: 400; }
  .agent-contact li { list-style: none; height: 70px; }

  .brand-bar {
    position: absolute; left: 0; right: 0; bottom: 0; height: 88px;
    background: var(--footer); display: flex; align-items: center; padding-left: 22px;
  }
  .brand-name { font-size: 56px; font-weight: 500; line-height: 1; color: var(--white); margin-right: 22px; }
  .brand-office { font-size: 14px; font-weight: 500; text-transform: uppercase; }
  .brand-office small { display: block; font-size: 9.5px; font-weight: 600; line-height: 13px; margin-top: 3px; }
</style>
</head>
<body>
<main class="slide">
  <div class="backdrop" role="img" aria-label="Bright living room interior photograph under a red colour overlay"></div>

  <p class="project-title">Project Title Here</p>
  <div class="project-rule"></div>

  <h1 class="thanks-heading">Thanks for your valuable times</h1>

  <div class="agent-portrait-frame">
    <div class="agent-portrait" role="img" aria-label="Portrait photo of the agent in a dark suit"></div>
  </div>

  <section class="agent-details">
    <h2 class="agent-name">Jonah Hale</h2>
    <p class="agent-office">Harbor Bay Partners<br>815 Shoreline Way, Ste 304<br>Ridgefield, GA 30512</p>
    <ul class="agent-contact">
      <li>O : 555.014.2290</li>
      <li>C : 555.018.6347</li>
      <li>www.harborwithhale.net</li>
    </ul>
  </section>

  <footer class="brand-bar">
    <span class="brand-name">HB</span>
    <div class="brand-office">Harbor Bay Partners
      <small>815 Shoreline Way, Ste 304<br>Ridgefield, GA 30512</small>
    </div>
  </footer>
</main>
</body>
</html>
```